Plastic Surgeon Needs a business card desing

I need a plastic surgeon business card, Im young , innovative , not afraid of thinking out of the box, What I dont like is human figures or scalpes as designing the card, because I think they are old fashion, I think my name is my strongest card, so I try to find the desing to be something elegant , simple , slick , stylish , radiant with carimsa!

Target Market(s)

PLastics Surgery Patients and doctors to have my data

Industry/Entity Type

Plastic

Contact Information for Business Card

phone numbers need to be legible , right now i have grey scales so they a not to legible

Font styles to use
Serif
Sans Serif

Requirements
Must have
• Personality, and it has to look like a doctor card, not a buisness man card, that is why i think it should be clean , clear , and legible
Nice to have
• Stylilsh, not to heavy card, in means of colors and logos, i think it should give a sensation of health
• Im not sure to have the logo of the hospital i work
Should not have
• human figures
• Hands
• Surgeons

```html
<!DOCTYPE html>
<html lang="es">
<head>
<meta charset="UTF-8">
<title>Dr. Mateo Larrosa – Cirugía Plástica</title>
<link rel="stylesheet" href="https://fonts.googleapis.com/css2?family=Bebas+Neue&display=swap">
<style>
  :root {
    --backdrop: #176a72;
    --card: #111214;
    --band-white: #ffffff;
    --band-grey: #a9aaad;
    --name-blue: #3d7fc6;
    --specialty-ink: #1a1a1c;
    --mark-silver: #d4d5d8;
  }
  html, body {
    margin: 0;
    padding: 0;
    width: 1200px;
    height: 710px;
    overflow: hidden;
    background: var(--backdrop);
  }
  .canvas {
    position: relative;
    width: 1200px;
    height: 710px;
    background: radial-gradient(ellipse at 30% 20%, #1d7e87 0%, var(--backdrop) 60%, #135a61 100%);
  }
  .card {
    position: absolute;
    left: 150px;
    top: 98px;
    width: 900px;
    height: 514px;
    background: var(--card);
    overflow: hidden;
    box-shadow: 0 18px 40px rgba(0, 0, 0, 0.35);
  }
  .wordmark {
    position: absolute;
    left: 0;
    right: 0;
    top: 150px;
    display: flex;
    justify-content: center;
    align-items: center;
    gap: 16px;
    font-family: "Bebas Neue", "Arial Narrow", sans-serif;
    font-size: 54px;
    letter-spacing: 6px;
    color: var(--mark-silver);
  }
  .wordmark-dot {
    width: 18px;
    height: 18px;
    border-radius: 50%;
    background: var(--mark-silver);
  }
  .name-band {
    position: absolute;
    left: 0;
    top: 340px;
    width: 560px;
    height: 72px;
    background: var(--band-white);
    display: flex;
    align-items: center;
    padding-left: 70px;
    box-sizing: border-box;
  }
  .doctor-name {
    margin: 0;
    font-family: "Bebas Neue", "Arial Narrow", sans-serif;
    font-size: 50px;
    line-height: 1;
    letter-spacing: 1px;
    color: var(--name-blue);
    font-weight: 400;
  }
  .specialty-band {
    position: absolute;
    left: 574px;
    top: 298px;
    width: 326px;
    height: 114px;
    background: var(--band-grey);
    display: flex;
    align-items: center;
    justify-content: center;
  }
  .specialty {
    margin: 0;
    font-family: "Bebas Neue", "Arial Narrow", sans-serif;
    font-size: 40px;
    letter-spacing: 4px;
    word-spacing: 22px;
    color: var(--specialty-ink);
    font-weight: 400;
  }
</style>
</head>
<body>
  <main class="canvas">
    <article class="card">
      <div class="wordmark">
        <span class="wordmark-dot"></span>
        <span class="wordmark-name">Larrosa</span>
      </div>
      <div class="name-band">
        <h1 class="doctor-name">Dr. Mateo Larrosa</h1>
      </div>
      <div class="specialty-band">
        <p class="specialty">Cirugia Plastica</p>
      </div>
    </article>
  </main>
</body>
</html>
```